" A TQR oferece uma franquia de assessoria técnica, onde o franqueado utiliza a metodologia validada e a tecnologia NexaForma para atender construtoras locais com serviços de planejamento e controle de obras e comunicação status da obra com o cliente final. "

```html
<!DOCTYPE html>
<html lang="pt-BR">
<head>
<meta charset="utf-8">
<title>TQR — Pasta institucional</title>
<link href="https://fonts.googleapis.com/css2?family=Montserrat:wght@400;500;600&display=swap" rel="stylesheet">
<style>
  :root {
    --backdrop: #d2cecb;
    --backdrop-light: #dedbd8;
    --folder-navy: #2b2944;
    --folder-navy-deep: #25233b;
    --ink-white: #ffffff;
    --ink-soft: #b9b8c8;
    --slit: #e6e4ee;
  }
  html, body {
    margin: 0;
    padding: 0;
    width: 1200px;
    height: 1200px;
    overflow: hidden;
    background: var(--backdrop);
  }
  .canvas {
    display: block;
    width: 1200px;
    height: 1200px;
  }
  .backdrop-frame { fill: var(--backdrop-light); }
  .backdrop-inner { fill: var(--backdrop); }
  .folder-cover { fill: var(--folder-navy); }
  .folder-pocket { fill: var(--folder-navy-deep); }
  .cover-gloss { fill: url(#gloss); }
  .card-slit { stroke: var(--slit); stroke-width: 1.2; stroke-linecap: round; }
  .brand-name {
    font-family: "Montserrat", sans-serif;
    font-weight: 600;
    fill: var(--ink-white);
  }
  .brand-tagline {
    font-family: "Montserrat", sans-serif;
    font-weight: 500;
    fill: var(--ink-white);
  }
  .contact-text {
    font-family: "Montserrat", sans-serif;
    font-weight: 400;
    font-size: 3px;
    fill: var(--ink-soft);
  }
  .contact-icon { fill: var(--ink-soft); }
</style>
</head>
<body>
<svg class="canvas" viewBox="0 0 500 500" xmlns="http://www.w3.org/2000/svg">
  <defs>
    <linearGradient id="gloss" x1="0" y1="0" x2="1" y2="1">
      <stop offset="0" stop-color="#ffffff" stop-opacity="0.16"/>
      <stop offset="1" stop-color="#ffffff" stop-opacity="0"/>
    </linearGradient>
  </defs>

  <!-- backdrop -->
  <rect class="backdrop-frame" x="0" y="0" width="500" height="500"/>
  <polygon class="backdrop-inner" points="14,14 486,14 486,486 14,486"/>

  <!-- folder cover -->
  <rect class="folder-cover" x="50" y="48" width="408" height="337"/>
  <polygon class="cover-gloss" points="390,48 458,48 458,120"/>

  <!-- pocket flap -->
  <path class="folder-pocket"
        d="M50,334 L258,334 L258,388 C205,398 170,440 128,470 L50,470 L50,458 L36,452 L36,346 L50,340 Z"/>
  <line class="card-slit" x1="137" y1="369" x2="150" y2="385"/>
  <line class="card-slit" x1="62" y1="402" x2="75" y2="418"/>

  <!-- main brand lockup -->
  <g class="brand-main">
    <text class="brand-name" x="364" y="204" font-size="44" text-anchor="middle" letter-spacing="2">TQR</text>
    <text class="brand-tagline" x="364" y="214" font-size="6.2" text-anchor="middle" letter-spacing="1.4">ASSESSORIA TÉCNICA</text>
    <text class="brand-tagline" x="364" y="223" font-size="6.2" text-anchor="middle" letter-spacing="5.2">DE OBRAS</text>
  </g>

  <!-- small brand lockup -->
  <g class="brand-small">
    <text class="brand-name" x="154" y="304" font-size="16" text-anchor="middle" letter-spacing="1">TQR</text>
    <text class="brand-tagline" x="154" y="309" font-size="2.3" text-anchor="middle" letter-spacing="0.7">ASSESSORIA TÉCNICA DE OBRAS</text>
  </g>

  <!-- contact row -->
  <g class="contact-row">
    <circle class="contact-icon" cx="78" cy="321" r="2.2"/>
    <text class="contact-text" x="83" y="320">+55 11 5555-0100</text>
    <text class="contact-text" x="83" y="325">+55 11 5555-0101</text>

    <rect class="contact-icon" x="126" y="319.2" width="5" height="3.6" rx="0.5"/>
    <text class="contact-text" x="134" y="320">contato@tqr.com.br</text>
    <text class="contact-text" x="134" y="325">www.tqr.com.br</text>

    <path class="contact-icon" d="M182,317 a2.2,2.2 0 0 1 2.2,2.2 c0,1.6 -2.2,4 -2.2,4 c0,0 -2.2,-2.4 -2.2,-4 a2.2,2.2 0 0 1 2.2,-2.2 z"/>
    <text class="contact-text" x="189" y="318">Rua Exemplo, 100</text>
    <text class="contact-text" x="189" y="322.5">Centro</text>
    <text class="contact-text" x="189" y="327">01000-000 · São Paulo · SP</text>
  </g>
</svg>
</body>
</html>
```